Harbor Lanterns: Walking Beside Young Ones Through Every Season

This book is about being a good father and how to parent them well so they are fully equipped to launch into the world when they become adults. It is an encouraging and practical guide that acknowledges the difficulties of being a good father and provides strategies for addressing them.

Target Market(s)

My target market is dads, or people that will gift this book to a dad that they know

```html
<!DOCTYPE html>
<html lang="en">
<head>
<meta charset="utf-8">
<title>Harbor Lanterns — Book Cover</title>
<link rel="stylesheet" href="https://fonts.googleapis.com/css2?family=Oswald:wght@600;700&family=Jost:wght@500;700&display=swap">
<style>
  :root {
    --page-bg: #d8b98a;
    --cover-top: #b9503f;
    --cover-mid: #d2653a;
    --glow-core: #fff2c2;
    --glow-warm: #f5a33a;
    --ridge-light: #f0a23a;
    --ridge-mid: #d8682e;
    --ground-dark: #2a0f10;
    --ground-deep: #1c0a0c;
    --ink-light: #ffffff;
    --ink-soft: #f6ede6;
  }
  * { box-sizing: border-box; margin: 0; padding: 0; }
  html, body {
    width: 1200px;
    height: 1200px;
    overflow: hidden;
    background: var(--page-bg);
  }
  .book-cover {
    position: absolute;
    left: 220px;
    top: 30px;
    width: 760px;
    height: 1140px;
    overflow: hidden;
    background: linear-gradient(180deg, var(--cover-top) 0%, var(--cover-mid) 55%, var(--glow-warm) 80%);
  }
  .sunset-scene {
    position: absolute;
    left: 0;
    right: 0;
    top: 470px;
    bottom: 0;
    background:
      radial-gradient(ellipse 55% 42% at 50% 52%, var(--glow-core) 0%, var(--glow-warm) 45%, rgba(210,101,58,0) 100%),
      linear-gradient(180deg, rgba(210,101,58,0) 0%, var(--ridge-light) 52%, var(--ridge-mid) 68%, var(--ground-dark) 84%, var(--ground-deep) 100%);
  }
  .title-block {
    position: absolute;
    top: 40px;
    left: 0;
    right: 0;
    text-align: center;
    color: var(--ink-light);
  }
  .title-main {
    font-family: 'Oswald', sans-serif;
    font-weight: 700;
    line-height: 1.02;
  }
  .title-main .title-lead {
    display: block;
    font-size: 118px;
    letter-spacing: 1px;
  }
  .title-main .title-key {
    display: block;
    font-size: 124px;
    text-transform: uppercase;
    letter-spacing: 1px;
  }
  .subtitle {
    margin-top: 18px;
    font-family: 'Jost', sans-serif;
    font-weight: 700;
    font-size: 34px;
    line-height: 1.3;
    letter-spacing: 1px;
    text-transform: uppercase;
  }
  .author-name {
    position: absolute;
    left: 0;
    right: 0;
    bottom: 42px;
    text-align: center;
    font-family: 'Jost', sans-serif;
    font-weight: 500;
    font-size: 46px;
    letter-spacing: 1px;
    color: var(--ink-soft);
  }
</style>
</head>
<body>
  <main class="book-cover">
    <div class="sunset-scene" role="img" aria-label="Silhouette of a father holding his young son's hand at sunset over layered orange mountains, with two bicycles standing in the grass"></div>
    <header class="title-block">
      <h1 class="title-main">
        <span class="title-lead">Harbor</span>
        <span class="title-key">Lanterns</span>
      </h1>
      <p class="subtitle">Walking Beside Young Ones<br>Through Every Season</p>
    </header>
    <p class="author-name">AUTHOR NAME</p>
  </main>
</body>
</html>
```